led light bulb promotional flyer

i need a flyer to help me sell my led light bulbs. I would like a single sided if possible that is if everything fits and looks nice or double sided if not. On the front i would like some details on led bulbs and the benefits they provide over standard incandescent light bulbs. I would like a header to include the pictures attached and my web page www.glowhausdirect.ie and my logo

also to include on front page: For the first time ever you can now replace your ordinary incandescent , halogen and CFL bulbs with more energy efficent LED bulbs.

www.glowhausdirect.ie can now offer you a complete range of LED bulbs on our website.

FACT: If you have 20 x 50w halogen spotlights in your home they are costing you €720 per year. If you switch to LED bulbs you can save as much as €600 per year which is a saving of 83%
In a domestic setting LED bulbs will pay for themselves within six months too one year depending on usage.

Lightbulbs in pubs , hotels and restaurants are typically switched on for 12 hours per day. At that level of usage energy efficient LED alternatives will pay for themselves in as little as one month. A small investment in LED bulbs will mean great savings in the long run.

Must be stated clearly on the front that delivery is FREE.

Target Market(s)

the target market are home owners in Ireland

Industry/Entity Type

Investment

Requirements
Must have
• on the back of the flyer i want to offer three LED bulbs for sale 3W GU10 LED BRAVOLT CHIP INSIDE cost €18 Can replace a 35w halogen lamp Lumens 258 warm white Lasts 30 times longer 25 years payes for itself within one year guaranteed for 1yearsaving per year V 35w halogen 92%

6w GU10 LED BRAVOLT CHIP INSIDE COST €22 Can replace a 50w halogen lamp lumens 320 warm white lasts 30 times longer 25 years Payes for it self within one year guaranteed for 1year Saving per year V 50w halogen 88%

7w LED bulb B22 base KELTA LED INSIDE COST €28 Can replace a 70 w incandecant bulb lumens 530 warm white Last 30 times longer 25 years payes for it self within one year guaranteed for 1 year
saving per year V 70w incandecent 90%
Nice to have
• Irish company.CE logo Rohs logo compliant paymarq verified green - energy saving enviromental save money please take a look at my web page for guidence

```html
<!DOCTYPE html>
<html lang="en">
<head>
<meta charset="utf-8">
<title>Glowhaus LED Bulbs Flyer</title>
<link href="https://fonts.googleapis.com/css2?family=Bebas+Neue&family=Overlock:wght@400;700&display=swap" rel="stylesheet">
<style>
  :root {
    --top-band: #050203;
    --wall-dark: #2a0409;
    --wall-mid: #4a0a14;
    --glow: #c81a38;
    --fact-red: #d8313b;
    --body-red: #e02446;
    --highlight-yellow: #f6ee9a;
    --floor-dark: #141416;
    --floor-mid: #26262a;
    --badge-red: #e2141c;
    --white: #ffffff;
  }
  * { margin: 0; padding: 0; box-sizing: border-box; }
  html, body { width: 846px; height: 1200px; overflow: hidden; background: #000; }
  .flyer {
    position: relative; width: 846px; height: 1200px; overflow: hidden;
    background: radial-gradient(ellipse 70% 55% at 50% 45%, var(--wall-mid), var(--wall-dark) 80%);
    font-family: "Overlock", sans-serif;
  }
  .top-band { position: absolute; left: 0; top: 0; width: 846px; height: 74px; background: var(--top-band); }
  .spotlight-glow {
    position: absolute; left: 0; top: 74px; width: 846px; height: 110px;
    background: linear-gradient(to bottom, var(--glow) 0%, rgba(200,26,56,0.45) 35%, rgba(74,10,20,0) 100%);
    opacity: 0.8;
  }
  .fact-heading {
    position: absolute; top: 206px; left: 0; width: 846px; text-align: center;
    font-family: "Bebas Neue", sans-serif; font-size: 104px; line-height: 1; font-weight: 400;
    color: var(--fact-red); letter-spacing: 1px;
  }
  .fact-copy {
    position: absolute; top: 366px; left: 100px; width: 646px; text-align: center;
    color: var(--body-red); font-size: 25.5px; line-height: 31px;
  }
  .fact-copy p + p { margin-top: 12px; }
  .headline {
    position: absolute; top: 652px; left: 103px; width: 640px; text-align: center;
    color: var(--highlight-yellow); font-size: 35px; line-height: 47px;
  }
  .floor {
    position: absolute; left: 0; top: 968px; width: 846px; height: 232px;
    background: linear-gradient(to bottom, var(--floor-mid), var(--floor-dark));
  }
  .bulb-photo {
    position: absolute; left: 288px; top: 868px; width: 280px; height: 232px;
    border-radius: 24px;
    background: linear-gradient(135deg, #e6e6e4 0%, #b4b4b6 50%, #7c7c80 100%);
  }
  .brand {
    position: absolute; left: 22px; top: 1078px; display: flex; align-items: center; gap: 10px;
    color: var(--white); font-size: 24px; font-weight: 700;
  }
  .brand-mark { width: 22px; height: 22px; background: var(--badge-red); }
  .web-address {
    position: absolute; left: 125px; top: 1150px; color: var(--white); font-size: 24px;
  }
  .delivery-badge { position: absolute; right: 0; bottom: 0; width: 236px; height: 236px; }
</style>
</head>
<body>
<div class="flyer">
  <div class="top-band"></div>
  <div class="spotlight-glow" role="img" aria-label="Row of five red stage spotlights shining down the wall"></div>

  <h1 class="fact-heading">Fact:</h1>

  <div class="fact-copy">
    <p>If you have 20 x 50w halogen spotlights in your home they are costing you €720 per year. If you switch to LED bulbs you can save as much as €600 per year which is a saving of 83%.</p>
    <p>In a domestic setting LED bulbs will pay for themselves within six months to one year depending on usage.</p>
  </div>

  <p class="headline">For the first time ever you can now replace your ordinary incandescent, halogen and CFL bulbs with more energy efficent LED bulbs.</p>

  <div class="floor" role="img" aria-label="Dark wooden stage floor"></div>

  <div class="bulb-photo" role="img" aria-label="Photo of a GU10 LED spotlight bulb with silver finned body resting on the stage floor"></div>

  <div class="brand"><span class="brand-mark"></span><span>Glowhaus</span></div>
  <div class="web-address">www.glowhausdirect.ie</div>

  <svg class="delivery-badge" viewBox="0 0 236 236" aria-label="Free delivery">
    <polygon points="236,0 236,236 0,236" fill="var(--badge-red)"/>
    <g transform="translate(150,168) rotate(-45)" fill="var(--white)" font-family="Overlock, sans-serif" text-anchor="middle">
      <text x="0" y="-8" font-size="50" font-weight="700">FREE</text>
      <text x="0" y="24" font-size="26">DELIVERY</text>
    </g>
  </svg>
</div>
</body>
</html>
```